Business card and (possibly) logo

Hi - we need a new business card.
We have an existing logo that we quite like but we are open to options.
We are an architectural firm - we specialize in upmarket residential work and apartment blocks.
We are chasing a business card at present but also want to extensively update our website going forward to attract a much higher level of client / investor / developer.
Our current logo is black, grey and yellow and based on the sun/moon temples in Mexico.
We are open to variations.
We want to communicate professionalism, trust, quality.
Our website is www.corvelldesignhouse.com.au - but note as above - we want to change the website as well to be a lot 'classier' and to appeal to a higher end market.

thanks

Target Market(s)

We are an architect firm - our target market is Developers and builders of high end houses and luxury apartment blocks. Also private home owners wanting to build excellent expensive houses. (ideally over $1m budgets)

Industry/Entity Type

Residential

Requirements
Must have
• Logo
Contact details;
Name
phone, mobile, email, web

```html
<!DOCTYPE html>
<html lang="en">
<head>
<meta charset="utf-8">
<title>Corvell Design House — Business Card</title>
<link href="https://fonts.googleapis.com/css2?family=Lato:wght@300;400;700;900&display=swap" rel="stylesheet">
<style>
  :root {
    --backdrop: #aab6b8;
    --card-white: #ffffff;
    --card-black: #050505;
    --ink-dark: #2a2627;
    --ink-light: #f2f2f2;
    --ink-muted: #9a9a9a;
    --accent-sun: #f2a71b;
  }
  * { margin: 0; padding: 0; box-sizing: border-box; }
  html, body {
    width: 1200px;
    height: 1000px;
    overflow: hidden;
    background: var(--backdrop);
    font-family: "Lato", Arial, sans-serif;
  }
  .canvas {
    position: relative;
    width: 1200px;
    height: 1000px;
  }
  .card {
    position: absolute;
    left: 250px;
    width: 700px;
    height: 400px;
    box-shadow: 0 6px 18px rgba(40, 55, 58, 0.25);
  }
  .card--front {
    top: 80px;
    background: var(--card-white);
    display: flex;
    align-items: center;
    justify-content: center;
  }
  .card--back {
    top: 520px;
    background: var(--card-black);
    color: var(--ink-light);
  }
  .brand {
    display: flex;
    align-items: center;
    gap: 22px;
  }
  .brand__mark {
    width: 26px;
    height: 26px;
    border-radius: 50%;
    background: var(--accent-sun);
    flex-shrink: 0;
  }
  .brand__name {
    font-weight: 900;
    color: var(--ink-dark);
    font-size: 62px;
    letter-spacing: -1px;
    line-height: 1;
  }
  .card--back .brand {
    position: absolute;
    top: 40px;
    left: 44px;
    gap: 12px;
  }
  .card--back .brand__mark {
    width: 14px;
    height: 14px;
  }
  .card--back .brand__name {
    color: var(--ink-light);
    font-size: 28px;
    letter-spacing: 0;
  }
  .contact {
    position: absolute;
    right: 44px;
    bottom: 40px;
    text-align: right;
    font-size: 17px;
    line-height: 1.35;
  }
  .contact__name {
    font-weight: 700;
    font-size: 24px;
    letter-spacing: 1px;
    margin-bottom: 8px;
  }
  .contact__label,
  .contact__phone { font-weight: 700; }
  .tagline {
    position: absolute;
    left: 44px;
    bottom: 40px;
    font-weight: 300;
    font-size: 17px;
    letter-spacing: 2px;
    color: var(--ink-muted);
  }
</style>
</head>
<body>
  <main class="canvas">
    <section class="card card--front" aria-label="Business card front">
      <div class="brand">
        <span class="brand__mark"></span>
        <span class="brand__name">corvell design house</span>
      </div>
    </section>

    <section class="card card--back" aria-label="Business card back">
      <div class="brand">
        <span class="brand__mark"></span>
        <span class="brand__name">corvell design house</span>
      </div>
      <address class="contact" style="font-style: normal;">
        <p class="contact__name">John Doe</p>
        <p>Address here</p>
        <p>and here too</p>
        <p><span class="contact__label">Telephone:</span> <span class="contact__phone">0123456789</span></p>
        <p>www.corvelldesignhouse.com.au</p>
        <p>www.corvelldesignhouse.co.au</p>
      </address>
      <p class="tagline">BUILDING DESIGN</p>
    </section>
  </main>
</body>
</html>
```